Original and striking logo and label design for a young handcrafted dry gin

I am starting a small artisan distillery venture to produce gin. The brand will be called Velmaris which means sunset. As my product is going to be new, modest and small-scale, but at the same time of high quality, I need to differentiate it through its packaging. As within my possibilities I have to resort to standard bottles on the market, it is important to have an original and different label. I want to be able to mark the premium character but at the same time handmade, between vintage or minimalist style (I have not decided yet which would be better). In the annex there is an "Inspiration.rar" file with images of other inspiring gin brands, which are a good example of the sense of excellence that the project must convey. I have already made some label models myself, but I am not satisfied, which I attach. Additionally, I enclose two models of bottles that interest me, with which the label should be able to adapt to both models. Please, if you are not at least at the level of the inspiration images, do not try to propose your model.

Target Market(s)

The product is mainly aimed at young people who appreciate high-quality beverages and who value an artisanal and sustainable product.

Logo Text

Velmaris

Font styles to use
Serif
Decorative
Script

Requirements
Must have
• Reference to the Portuguese sunset (at sea). Reference to what is handcrafted; Portuguese. They must include the following slogan: "Distilled in the glow of the
Portuguese Sunset". The label should allow the following information to be completed by hand: Date distilled; Distiller; Bottle No.; Batch No.

```html
<!DOCTYPE html>
<html lang="en">
<head>
<meta charset="utf-8">
<title>Velmaris Gin Label</title>
<link rel="stylesheet" href="https://fonts.googleapis.com/css2?family=Barlow+Condensed:wght@500;600;700&family=Parisienne&display=swap">
<style>
  :root {
    --backdrop: #d9d9d9;
    --paper: #fbfbfa;
    --ink: #3b3b37;
    --rule: #4a4a46;
    --copper-dark: #b4471c;
    --copper: #d6783f;
    --copper-light: #f6e2c0;
  }
  * { box-sizing: border-box; margin: 0; padding: 0; }
  html, body { width: 1200px; height: 1200px; overflow: hidden; }
  body {
    background: var(--backdrop);
    display: flex;
    align-items: center;
    justify-content: center;
    font-family: "Barlow Condensed", "Arial Narrow", sans-serif;
    color: var(--ink);
  }
  .label {
    width: 840px;
    height: 1040px;
    background: var(--paper);
    position: relative;
    box-shadow: 0 6px 24px rgba(0,0,0,0.12);
  }
  .lockup {
    position: absolute;
    top: 70px;
    left: 0;
    right: 0;
    text-align: center;
  }
  .lockup__tagline {
    font-weight: 600;
    font-size: 40px;
    letter-spacing: 2px;
    text-transform: uppercase;
  }
  .lockup__dot {
    width: 170px;
    height: 170px;
    border-radius: 50%;
    border: 4px solid var(--ink);
    margin: 22px auto 0;
  }
  .lockup__name {
    font-weight: 700;
    font-size: 96px;
    line-height: 1;
    letter-spacing: 4px;
    text-transform: uppercase;
    margin-top: 18px;
  }
  .lockup__sub {
    font-weight: 600;
    font-size: 44px;
    letter-spacing: 1px;
    text-transform: uppercase;
    margin-top: 4px;
  }
  .record {
    position: absolute;
    top: 562px;
    left: 76px;
    width: 656px;
    display: grid;
    grid-template-columns: 1fr 1fr;
    column-gap: 34px;
    border-bottom: 4px solid var(--rule);
  }
  .record__column { position: relative; }
  .record__column--right::before {
    content: "";
    position: absolute;
    left: -18px;
    top: 26px;
    width: 4px;
    height: 92px;
    background: var(--rule);
  }
  .record__field {
    border-top: 3px solid var(--rule);
    height: 70px;
    padding: 10px 8px 0;
    font-weight: 500;
    font-size: 27px;
  }
  .slogan {
    position: absolute;
    top: 756px;
    left: 0;
    right: 0;
    text-align: center;
    font-family: "Parisienne", cursive;
    font-size: 46px;
  }
  .specs {
    position: absolute;
    top: 856px;
    left: 0;
    right: 0;
    display: flex;
    justify-content: center;
    font-weight: 600;
    font-size: 30px;
  }
  .specs__item { padding: 0 20px; }
  .specs__item + .specs__item { border-left: 4px solid var(--ink); }
  .copper-band {
    position: absolute;
    left: 0;
    right: 0;
    bottom: 0;
    height: 112px;
    background: linear-gradient(90deg, var(--copper-dark) 0%, var(--copper) 30%, var(--copper-light) 44%, var(--copper) 62%, var(--copper-dark) 100%);
  }
</style>
</head>
<body>
  <main class="label">
    <header class="lockup">
      <p class="lockup__tagline">• Tuga Distilled Gin •</p>
      <div class="lockup__dot"></div>
      <h1 class="lockup__name">Velmaris</h1>
      <p class="lockup__sub">Handcrafted</p>
    </header>

    <section class="record">
      <div class="record__column">
        <div class="record__field">Date distilled:</div>
        <div class="record__field">Bottle No.:</div>
      </div>
      <div class="record__column record__column--right">
        <div class="record__field">Distiller:</div>
        <div class="record__field">Batch No.:</div>
      </div>
    </section>

    <p class="slogan">Distilled in the Glow of the Portuguese Sunset</p>

    <p class="specs">
      <span class="specs__item">43% vol.</span>
      <span class="specs__item">70 cl</span>
    </p>

    <div class="copper-band"></div>
  </main>
</body>
</html>
```